Business Card Design Project

Looking for a simple and stylish business card. We are an Advertising Company. The card Must feature the company logo (attached) and also this info.
p: 0481629054
e: sales@rv-promo.com.au
w: www.rv-promo.com.au
We Advertise mainly using TV screens featured in restaurants and cafe. See website for more about the business.
Not really looking for a plain background, but at the same time do not want to much happening in the Background. I am not really to fussy though with the design or the colour scheme, and I am leaving the creativity part up to you creative designers.

```html
<!DOCTYPE html>
<html lang="en">
<head>
<meta charset="utf-8">
<title>RVPROMO Business Card</title>
<link rel="stylesheet" href="https://fonts.googleapis.com/css2?family=Montserrat:ital,wght@0,400;0,500;0,700;1,700&display=swap">
<style>
  :root {
    --page-bg: #ffffff;
    --card-white: #ffffff;
    --brand-pink: #e8205a;
    --brand-blue: #17479b;
    --panel-top: #3e3190;
    --panel-bottom: #3d55a6;
    --gold-a: #f3c84a;
    --gold-b: #fbf2cf;
    --gold-c: #e0a619;
    --text-light: #ffffff;
  }
  html, body {
    margin: 0;
    padding: 0;
    width: 1200px;
    height: 1000px;
    overflow: hidden;
    background: var(--page-bg);
    font-family: "Montserrat", sans-serif;
  }
  .business-card {
    position: absolute;
    left: 222px;
    top: 273px;
    width: 756px;
    height: 432px;
    background: var(--card-white);
    box-shadow: 3px 4px 6px rgba(0, 0, 0, 0.28);
    overflow: hidden;
  }
  .brand-name {
    position: absolute;
    left: 0;
    right: 0;
    top: 42px;
    margin: 0;
    text-align: center;
    font-weight: 500;
    font-size: 118px;
    line-height: 1;
    letter-spacing: 4px;
    color: var(--brand-blue);
  }
  .accent-band {
    position: absolute;
    left: 0;
    top: 215px;
    width: 100%;
    height: 11px;
    background: var(--brand-pink);
  }
  .gold-band {
    position: absolute;
    left: 0;
    top: 226px;
    width: 100%;
    height: 12px;
    background: linear-gradient(90deg,
      var(--gold-b) 0%, var(--gold-a) 10%, var(--gold-b) 20%, var(--gold-a) 32%,
      var(--gold-c) 45%, var(--gold-b) 55%, var(--gold-a) 65%, var(--gold-c) 78%,
      var(--gold-b) 90%, var(--gold-a) 100%);
  }
  .info-panel {
    position: absolute;
    left: 0;
    top: 238px;
    width: 100%;
    height: 194px;
    background: linear-gradient(180deg, var(--panel-top) 0%, var(--panel-bottom) 100%);
    color: var(--text-light);
  }
  .contact-list {
    position: absolute;
    left: 38px;
    top: 46px;
    margin: 0;
    padding: 0;
    list-style: none;
    font-size: 21px;
    line-height: 42px;
  }
  .contact-label { font-weight: 400; }
  .contact-value { font-weight: 700; }
  .person {
    position: absolute;
    right: 40px;
    top: 84px;
    text-align: right;
    font-size: 23px;
    line-height: 42px;
    font-weight: 700;
  }
  .person-role { font-style: italic; display: block; }
  .person-name { display: block; }
</style>
</head>
<body>
  <div class="business-card">
    <h1 class="brand-name">RVPROMO</h1>
    <div class="accent-band"></div>
    <div class="gold-band"></div>
    <div class="info-panel">
      <ul class="contact-list">
        <li><span class="contact-label">p: </span><span class="contact-value">0481629054</span></li>
        <li><span class="contact-label">e: </span><span class="contact-value">sales@rv-promo.com.au</span></li>
        <li><span class="contact-label">w: </span><span class="contact-value">www.rv-promo.com.au</span></li>
      </ul>
      <div class="person">
        <span class="person-role">Managing Director</span>
        <span class="person-name">Mark Tevaliso</span>
      </div>
    </div>
  </div>
</body>
</html>
```